Verdanel Waste Website Design

Our new start-up needs a website design. We plan to help businesses find more sustainable ways to manage their waste. Our initial website aims to gather contact data from potential business customers and comprehensive information from waste facilities and waste transporters. We have a logo design (attached) which we would like included in the website design. I have also attached a number of pages that describe what information should appear on each page as well as a web design brief file that describes the look we are after.

```html
<!DOCTYPE html>
<html lang="en">
<head>
<meta charset="utf-8">
<title>Verdanel Waste</title>
<link rel="stylesheet" href="https://fonts.googleapis.com/css2?family=Arimo:wght@400;700&display=swap">
<style>
  :root {
    --leaf: #6a9a2c;
    --lime: #aed136;
    --olive: #56661c;
    --ink: #222222;
    --nav-dark: #4a4a4a;
    --nav-text: #444444;
    --white: #ffffff;
    --sky-top: #2f6fb5;
    --sky-mid: #5f9bd6;
    --rubble: #7b7466;
  }
  * { box-sizing: border-box; margin: 0; padding: 0; }
  html, body { width: 1200px; height: 1200px; overflow: hidden; background: var(--white); }
  body { position: relative; font-family: "Arimo", Arial, sans-serif; color: var(--ink); }

  .brand { position: absolute; left: 256px; top: 21px; display: flex; align-items: center; gap: 8px; }
  .brand-dot { width: 34px; height: 34px; border-radius: 50%; background: var(--lime); }
  .brand-name { font-size: 22px; font-weight: 700; color: var(--nav-dark); letter-spacing: 0.3px; }

  .main-nav { position: absolute; left: 592px; top: 29px; display: flex; height: 28px; }
  .main-nav a { display: flex; align-items: center; padding: 0 9px; font-size: 11.5px; color: var(--nav-text); text-decoration: none; }
  .main-nav a.is-current { background: var(--nav-dark); color: var(--white); padding: 0 11px; }

  .header-rule { position: absolute; left: 121px; top: 79px; width: 960px; height: 5px; background: var(--leaf); }

  .hero { position: absolute; left: 121px; top: 84px; width: 960px; height: 466px; overflow: hidden; }
  .hero-photo { position: absolute; inset: 0; background: linear-gradient(180deg, var(--sky-top) 0%, var(--sky-mid) 55%, #a9b7c2 75%, var(--rubble) 100%); }
  .hero-title { position: absolute; left: 427px; top: 91px; font-size: 40px; color: var(--white); font-weight: 400; white-space: nowrap; }
  .hero-sub { position: absolute; left: 427px; top: 140px; font-size: 29px; color: var(--white); font-weight: 400; }
  .hero-actions { position: absolute; left: 429px; top: 186px; display: flex; gap: 10px; }
  .hero-actions a { width: 138px; height: 33px; background: var(--lime); color: var(--nav-dark); font-size: 11px; line-height: 11.5px; text-align: center; text-decoration: none; display: flex; align-items: center; justify-content: center; }

  .services { position: absolute; top: 653px; left: 0; width: 1200px; }
  .service { position: absolute; top: 0; }
  .service h2 { font-size: 19px; font-weight: 400; color: var(--leaf); margin-bottom: 13px; white-space: nowrap; }
  .service p { font-size: 11.5px; line-height: 19.2px; color: var(--ink); padding-left: 2px; }
  .service a { color: var(--leaf); text-decoration: none; }

  .site-footer { position: absolute; left: 121px; top: 978px; width: 960px; height: 67px; background: var(--olive); }
  .site-footer p { position: absolute; left: 113px; top: 24px; font-size: 11.5px; color: var(--white); }

  .signup { position: absolute; left: 121px; top: 1045px; width: 960px; height: 155px; background: var(--lime); }
  .signup-title { position: absolute; left: 110px; top: 26px; font-size: 19.5px; font-weight: 400; color: var(--ink); }
  .signup-text { position: absolute; left: 110px; top: 69px; font-size: 14.5px; color: var(--ink); }
  .signup-email { position: absolute; left: 524px; top: 65px; width: 189px; height: 24px; background: var(--white); border: none; padding-left: 7px; font-family: inherit; font-size: 11.5px; color: var(--ink); }
  .signup-send { position: absolute; left: 718px; top: 65px; width: 119px; height: 24px; background: var(--olive); color: var(--white); border: none; font-family: inherit; font-size: 15px; letter-spacing: 1.5px; }
  .signup-close { position: absolute; left: 839px; top: 25px; width: 18px; height: 18px; }
</style>
</head>
<body>
  <header>
    <div class="brand"><span class="brand-dot"></span><span class="brand-name">Verdanel Waste</span></div>
    <nav class="main-nav">
      <a class="is-current" href="#">ABOUT US</a>
      <a href="#">WHAT WE DO</a>
      <a href="#">RESOURCES</a>
      <a href="#">CONTACT US</a>
    </nav>
    <div class="header-rule"></div>
  </header>

  <section class="hero">
    <div class="hero-photo" role="img" aria-label="Landfill site under a blue sky with a tipping container and a yellow bulldozer on piles of waste"></div>
    <h1 class="hero-title">Welcome to Verdanel Waste</h1>
    <p class="hero-sub">Take control of your waste here</p>
    <div class="hero-actions">
      <a href="#">WASTE<br>PRODUCERS</a>
      <a href="#">WASTE<br>FACILITIES</a>
      <a href="#">WASTE<br>TRANSPORTERS</a>
    </div>
  </section>

  <section class="services">
    <article class="service" style="left:230px;width:234px">
      <h2>WASTE PRODUCERS</h2>
      <p>At Verdanel Waste, we know that dealing with waste is expensive and complicated for everyone, especially businesses. To make matters worse, most waste is not reused or recycled. Given the expense and complexity, shouldn’t doing the right thing for the planet be part of the price?&nbsp; <a href="#">READ MORE</a></p>
    </article>
    <article class="service" style="left:495px;width:212px">
      <h2>WASTE FACILITIES</h2>
      <p style="padding-left:4px">By registering with Verdanel Waste, waste facilities and businesses that receive wastes are visible via the Verdanel Waste search tool. Searches are sorted by sustainability and location so it is important to supply accurate location details for your waste facilities. <a href="#">READ MORE</a></p>
    </article>
    <article class="service" style="left:745px;width:225px">
      <h2>WASTE TRANSPORTERS</h2>
      <p style="padding-left:3px">Waste transporters and controlled waste carriers provide a vital link between waste producers and waste facilities. The safe transport of waste is an essential economic and community service. <a href="#">READ MORE</a></p>
    </article>
  </section>

  <footer class="site-footer">
    <p>Copyright 2018 Verdanel Waste. All Rights Reserved.</p>
  </footer>

  <aside class="signup">
    <h2 class="signup-title">Welcome to Verdanel Waste. We are just getting started.</h2>
    <p class="signup-text">Please register your email address to receive updates from us.</p>
    <input class="signup-email" type="text" placeholder="Your email address" aria-label="Your email address">
    <button class="signup-send" type="button">SEND</button>
    <svg class="signup-close" viewBox="0 0 18 18" aria-label="Close">
      <rect x="0.5" y="0.5" width="17" height="17" fill="var(--olive)" stroke="var(--white)"/>
      <path d="M2 2 L16 16 M16 2 L2 16" stroke="var(--white)" stroke-width="1.3"/>
    </svg>
  </aside>
</body>
</html>
```